Brightwell Auto Care 4x9 Rack Card

Design a 4" wide by 9" tall rack card printed front and back using the copy, logo and images uploaded below. I am also uploading a current flyer so you can see the typestyles we use. I will get the exact name of the font for you ASAP. Also will be uploading some before and after pictures for the back of the rack card

Target Market(s)

Affluent consumers who need their car cleaned and detailed in a meticulous fashion

Requirements
Must have
• Under the logo, put the words...... Premium Steam Detailing & Ceramic Coating.........also put ther following wording on the front side: Get Steamed! We use steam to clean your vehicle helping save millions of gallons of water and protecting our rivers, streams and lakes from runoff.
Nice to have
• a screened back background of hexagons might be nice

```html
<!DOCTYPE html>
<html lang="en">
<head>
<meta charset="utf-8">
<title>Brightwell Auto Care – Rack Card</title>
<link rel="stylesheet" href="https://fonts.googleapis.com/css2?family=Montserrat:wght@400;600;700;800&family=Oswald:wght@500&family=Arimo:ital,wght@0,400;0,700;1,400;1,700&family=Great+Vibes&display=swap">
<style>
  :root{
    --stage:#9a9a9a;
    --white:#ffffff;
    --blue:#3b7fd0;
    --blue-light:#5a9ce6;
    --blue-deep:#2c6dbf;
    --green:#6fae4c;
    --green-light:#84c05c;
    --grey-line:#c9ccd0;
    --text-blue:#3f7ed0;
    --photo-dark:#3a4048;
    --photo-mid:#8a9098;
  }
  *{box-sizing:border-box;margin:0;padding:0}
  html,body{width:1200px;height:1200px;overflow:hidden;background:var(--stage)}
  .stage{position:relative;width:1200px;height:1200px}
  .card{position:absolute;top:161px;width:387px;height:869px;background:var(--white);overflow:hidden;box-shadow:0 2px 6px rgba(0,0,0,.35)}
  .card--front{left:178px}
  .card--back{left:635px}
  .card svg.art{position:absolute;left:0;top:0}
  .t{position:absolute;left:0;right:0;text-align:center;transform:translateY(-50%);white-space:nowrap}

  /* front */
  .brand{font-family:"Montserrat",sans-serif;font-weight:700;color:var(--green);font-size:31px;letter-spacing:3px;line-height:1}
  .tagline{font-family:"Oswald",sans-serif;font-weight:500;color:var(--green);font-size:12.5px;letter-spacing:.2px}
  .intro-head{font-family:"Arimo",sans-serif;font-weight:700;font-style:italic;color:var(--text-blue);font-size:15px}
  .intro-body{font-family:"Arimo",sans-serif;color:var(--text-blue);font-size:12.6px;line-height:14.6px;white-space:normal;left:80px;right:80px;transform:none}
  .address{font-family:"Arimo",sans-serif;color:var(--white);font-size:13px;left:-10px}
  .cta-pill{position:absolute;left:27px;top:722px;width:312px;height:29px;border-radius:15px;background:linear-gradient(180deg,#e9e9e9,#b9b9b9 55%,#d8d8d8);border:1px solid #f4f4f4;font-family:"Arimo",sans-serif;font-style:italic;font-weight:700;color:#444;font-size:16.5px;text-align:center;line-height:27px}
  .phone{font-family:"Montserrat",sans-serif;font-weight:700;color:var(--white);font-size:17.5px;left:-12px;letter-spacing:.3px}

  /* back */
  .photo{position:absolute;background:linear-gradient(135deg,var(--photo-mid),var(--photo-dark))}
  .photo--framed{outline:1px solid var(--green);outline-offset:2px}
  .tag{position:absolute;background:var(--blue);color:var(--white);font-family:"Montserrat",sans-serif;font-weight:700;font-size:10px;letter-spacing:1.6px;display:flex;align-items:center;justify-content:center}
  .tag--vertical{writing-mode:vertical-rl;transform:rotate(180deg)}
  .service{font-family:"Montserrat",sans-serif;font-weight:800;color:var(--white);font-size:15px;letter-spacing:.2px}
  .price{font-family:"Montserrat",sans-serif;font-weight:400;color:var(--white);font-size:16px}
  .divider{position:absolute;left:155px;top:580px;width:72px;height:2px;background:var(--white)}
  .script{font-family:"Great Vibes",cursive;color:var(--white);font-size:29px}
  .slogan{font-family:"Montserrat",sans-serif;font-weight:800;color:var(--white);font-size:22px}
  .quote{font-family:"Arimo",sans-serif;font-style:italic;color:var(--white);font-size:17.5px}
  .big-phone{font-family:"Montserrat",sans-serif;font-weight:800;color:var(--white);font-size:37px;letter-spacing:1px}
  .web{font-family:"Arimo",sans-serif;color:var(--white);font-size:21px}
</style>
</head>
<body>
<div class="stage">

  <!-- FRONT -->
  <section class="card card--front">
    <svg class="art" width="387" height="869" viewBox="0 0 387 869">
      <defs>
        <linearGradient id="photoTone" x1="0" y1="0" x2="1" y2="1">
          <stop offset="0" stop-color="#2e3238"/>
          <stop offset=".45" stop-color="#9aa3ad"/>
          <stop offset=".7" stop-color="#c4ccd4"/>
          <stop offset="1" stop-color="#1f2328"/>
        </linearGradient>
        <linearGradient id="sidePhoto" x1="0" y1="0" x2="0" y2="1">
          <stop offset="0" stop-color="#1c1c1c"/>
          <stop offset=".5" stop-color="#c9b79c"/>
          <stop offset="1" stop-color="#8a7a64"/>
        </linearGradient>
        <linearGradient id="blueHex" x1="0" y1="0" x2="1" y2="1">
          <stop offset="0" stop-color="#2c6dbf"/>
          <stop offset="1" stop-color="#5a9ce6"/>
        </linearGradient>
        <polygon id="hex" points="-42,0 -21,-36 21,-36 42,0 21,36 -21,36"/>
      </defs>

      <g role="img" aria-label="Honeycomb photo collage of a detailer hand-polishing the hood of a silver sports car" fill="url(#photoTone)">
        <use href="#hex" x="60" y="72"/><use href="#hex" x="60" y="152"/><use href="#hex" x="60" y="232"/>
        <use href="#hex" x="130" y="36"/><use href="#hex" x="130" y="112"/><use href="#hex" x="130" y="192"/><use href="#hex" x="130" y="272"/>
        <use href="#hex" x="200" y="72"/><use href="#hex" x="200" y="152"/><use href="#hex" x="200" y="232"/>
        <use href="#hex" x="270" y="36"/><use href="#hex" x="270" y="112"/><use href="#hex" x="270" y="192"/><use href="#hex" x="270" y="272"/>
        <use href="#hex" x="333" y="72"/><use href="#hex" x="333" y="152"/><use href="#hex" x="333" y="232"/>
      </g>

      <polygon points="0,425 84,567 0,733" fill="var(--green)"/>
      <polygon points="0,760 0,869 76,869" fill="var(--green)"/>
      <polygon points="387,760 387,869 310,869" fill="var(--green-light)"/>
      <polygon role="img" aria-label="Photo of a detailer steam-cleaning a car's front grille" points="387,404 298,566 387,733" fill="url(#sidePhoto)"/>
      <line x1="0" y1="418" x2="86" y2="565" stroke="var(--grey-line)" stroke-width="3"/>
      <line x1="387" y1="400" x2="296" y2="565" stroke="var(--grey-line)" stroke-width="3"/>
      <polygon points="86,571 284,571 385,733 300,880 86,880 0,733" fill="url(#blueHex)" stroke="var(--grey-line)" stroke-width="5"/>
    </svg>

    <div class="t brand" style="top:392px">BRIGHTWELL</div>
    <div class="t brand" style="top:428px;font-size:27px;letter-spacing:9px">AUTO CARE</div>
    <div class="t tagline" style="top:448px">PREMIUM STEAM DETAILING &amp; CERAMIC COATING</div>

    <div class="t intro-head" style="top:474px">GET STEAMED!</div>
    <p class="t intro-body" style="top:483px;left:82px;right:82px">We use steam to clean your vehicle helping save millions of gallons of water &amp; protecting our rivers, streams &amp; lakes from runoff.</p>

    <div class="t address" style="top:597px">2140 Larkspur Avenue @</div>
    <div class="t address" style="top:615px;letter-spacing:-.4px">The Larkspur Commons</div>
    <div class="t address" style="top:632px">Boulder</div>
    <div class="t address" style="top:657px">58 Alder Lane</div>
    <div class="t address" style="top:675px">Snowmass Village</div>
    <div class="t address" style="top:702px">412 Ridgeline Rd #108, Avon</div>

    <div class="cta-pill">Call for information &amp; scheduling</div>

    <div class="t phone" style="top:777px">Boulder&nbsp; (720) 555-0142</div>
    <div class="t phone" style="top:798px">Vail&nbsp; (970) 555-0187</div>
    <div class="t phone" style="top:819px">Aspen/Snowmass</div>
    <div class="t phone" style="top:841px">(970) 555-0163</div>
  </section>

  <!-- BACK -->
  <section class="card card--back">
    <svg class="art" width="387" height="869" viewBox="0 0 387 869">
      <defs>
        <linearGradient id="blueHex2" x1="0" y1="0" x2="1" y2="1">
          <stop offset="0" stop-color="#2c6dbf"/>
          <stop offset="1" stop-color="#5a9ce6"/>
        </linearGradient>
      </defs>
      <rect x="0" y="190" width="387" height="679" fill="var(--blue)"/>
      <polygon points="0,210 76,318 0,506" fill="var(--green)"/>
      <polygon points="387,560 387,869 315,869 387,760" fill="var(--green)"/>
      <polygon points="387,506 310,694 387,730" fill="var(--green)"/>
      <rect x="0" y="284" width="387" height="30" fill="#e6e8ea"/>
      <polygon points="0,190 50,190 78,284 0,284" fill="var(--green)"/>
      <polygon points="340,190 387,190 387,300 320,300" fill="var(--blue-deep)"/>
      <polygon points="76,318 315,318 387,506 315,694 76,694 0,506" fill="url(#blueHex2)" stroke="var(--grey-line)" stroke-width="5"/>
      <polygon points="73,708 300,708 387,860 387,880 0,880 0,840" fill="var(--green)" stroke="var(--grey-line)" stroke-width="5"/>
    </svg>

    <div class="photo" role="img" aria-label="Engine bay before cleaning, covered in leaves" style="left:19px;top:22px;width:156px;height:79px"></div>
    <div class="tag tag--vertical" style="left:175px;top:22px;width:19px;height:79px">BEFORE</div>

    <div class="photo photo--framed" role="img" aria-label="Engine bay after steam cleaning" style="left:19px;top:113px;width:156px;height:80px"></div>
    <div class="tag tag--vertical" style="left:175px;top:113px;width:19px;height:80px">AFTER</div>

    <div class="photo" role="img" aria-label="Dashboard and console before detailing" style="left:205px;top:22px;width:76px;height:171px"></div>
    <div class="tag" style="left:205px;top:176px;width:76px;height:17px">BEFORE</div>

    <div class="photo photo--framed" role="img" aria-label="Dashboard and console after detailing" style="left:290px;top:22px;width:80px;height:171px"></div>
    <div class="tag" style="left:290px;top:176px;width:80px;height:17px">AFTER</div>

    <div class="photo" role="img" aria-label="Dirty car interior floor before detailing" style="left:19px;top:204px;width:175px;height:79px"></div>
    <div class="tag" style="left:114px;top:266px;width:80px;height:17px">BEFORE</div>

    <div class="photo photo--framed" role="img" aria-label="Clean car interior after detailing" style="left:205px;top:204px;width:165px;height:79px"></div>
    <div class="tag" style="left:205px;top:266px;width:80px;height:17px">AFTER</div>

    <div class="t service" style="top:356px">PREMIUM STEAM WASHES</div>
    <div class="t price" style="top:377px">starting at $100 &amp; up</div>
    <div class="t service" style="top:406px">FULL STEAM DETAILING</div>
    <div class="t price" style="top:427px">starting at $275 &amp; up</div>
    <div class="t service" style="top:455px">PAINT CORRECTION</div>
    <div class="t service" style="top:473px">(MULTI-STAGE POLISHING)</div>
    <div class="t price" style="top:495px">starting at $650 &amp; up</div>
    <div class="t service" style="top:522px">HEADLIGHT RESTORATION - $110</div>
    <div class="t service" style="top:551px">ENGINE STEAM CLEANING - $75</div>
    <div class="divider"></div>
    <div class="t script" style="top:616px">Fall In Love With</div>
    <div class="t slogan" style="top:642px">YOUR CAR AGAIN!</div>

    <div class="t quote" style="top:738px">Ceramic Coating-</div>
    <div class="t quote" style="top:761px">Call or visit us for a Quote</div>
    <div class="t big-phone" style="top:801px">(970) 555-0163</div>
    <div class="t web" style="top:828px">www.brightwellautocare.com</div>
  </section>

</div>
</body>
</html>
```